Pharmacist turned chef in Key West Fl needs a logo design

I am looking for a professional looking business card that says who I am and what I do. For example Chef Dale Morrow, natural organic and health supportive cooking. Phone 305-617-4289 email dalemorrow@quillpost.example web www.thehearthremedy.example, Key West fl. The color or colors should have some green and other colors that look good together that stimulate appetite and give a clean healthy image. To help with a thought process, words like food as medicine, medicine is food, good nutrition is health but at the same time I do not want a lot of medical symbols that me it look clinical. Any questions please contact me.

```html
<!DOCTYPE html>
<html lang="en">
<head>
<meta charset="utf-8">
<title>Chef Dale Morrow – Business Card Colour Options</title>
<link rel="stylesheet" href="https://fonts.googleapis.com/css2?family=Mulish:wght@300;400;600&display=swap">
<style>
  :root {
    --orange: #f15a29;
    --blue: #0d4ea2;
    --teal: #00667a;
    --green: #007a3d;
    --grey: #58585a;
    --ink: #333333;
    --paper: #ffffff;
  }
  html, body {
    margin: 0;
    padding: 0;
    width: 1200px;
    height: 1000px;
    overflow: hidden;
    background: var(--paper);
    font-family: "Mulish", Arial, sans-serif;
  }
  .board {
    position: relative;
    width: 1200px;
    height: 1000px;
  }
  .option-label {
    position: absolute;
    width: 492px;
    text-align: center;
    font-size: 36px;
    font-weight: 300;
    color: var(--teal);
    line-height: 1;
  }
  .card {
    position: absolute;
    width: 490px;
    height: 280px;
    border: 1px solid var(--ink);
    background: var(--paper);
    overflow: hidden;
  }
  .contact {
    position: absolute;
    right: 27px;
    top: 16px;
    text-align: right;
    font-size: 16px;
    line-height: 21px;
    font-weight: 400;
  }
  .contact .email { color: var(--contact-colour); }
  .contact .email .at { color: var(--at-colour); }
  .contact .phone { color: var(--contact-colour); }
  .contact .city { color: var(--orange); }
  .chef-name {
    position: absolute;
    left: 0;
    right: 0;
    top: 92px;
    text-align: center;
    font-size: 38px;
    font-weight: 600;
    color: var(--green);
    letter-spacing: 0.5px;
  }
  .tagline {
    position: absolute;
    left: 0;
    right: 0;
    top: 209px;
    text-align: center;
    font-size: 18.5px;
    font-weight: 400;
    color: var(--tagline-colour);
  }
  .web-band {
    position: absolute;
    left: 0;
    right: 0;
    bottom: 0;
    height: 41px;
    background: var(--band-colour);
    color: var(--paper);
    text-align: center;
    font-size: 20px;
    line-height: 41px;
    font-weight: 400;
  }
  .card--a { left: 74px; top: 128px; --contact-colour: var(--teal); --at-colour: var(--orange); --tagline-colour: var(--orange); --band-colour: var(--teal); }
  .card--b { left: 642px; top: 128px; --contact-colour: var(--blue); --at-colour: var(--orange); --tagline-colour: var(--orange); --band-colour: var(--green); }
  .card--c { left: 74px; top: 539px; --contact-colour: var(--grey); --at-colour: var(--orange); --tagline-colour: var(--green); --band-colour: var(--orange); }
  .card--d { left: 642px; top: 539px; --contact-colour: var(--blue); --at-colour: var(--blue); --tagline-colour: var(--green); --band-colour: var(--blue); }
  .card--d .contact .city { color: var(--blue); }
  .palette {
    position: absolute;
    left: 819px;
    top: 927px;
  }
</style>
</head>
<body>
<main class="board">

  <div class="option-label" style="left:58px; top:80px;">a</div>
  <div class="option-label" style="left:633px; top:80px;">b</div>
  <div class="option-label" style="left:58px; top:485px;">c</div>
  <div class="option-label" style="left:640px; top:485px;">d</div>

  <section class="card card--a">
    <div class="contact">
      <div class="email">dalemorrow<span class="at">@</span>quillpost.example</div>
      <div class="phone">305.617.4289</div>
      <div class="city">Key West, FL</div>
    </div>
    <div class="chef-name">Chef Dale Morrow</div>
    <div class="tagline">Natural Organic &amp; Health Supportive Cooking</div>
    <div class="web-band">TheHearthRemedy.example</div>
  </section>

  <section class="card card--b">
    <div class="contact">
      <div class="email">dalemorrow<span class="at">@</span>quillpost.example</div>
      <div class="phone">305.617.4289</div>
      <div class="city">Key West, FL</div>
    </div>
    <div class="chef-name">Chef Dale Morrow</div>
    <div class="tagline">Natural Organic &amp; Health Supportive Cooking</div>
    <div class="web-band">TheHearthRemedy.example</div>
  </section>

  <section class="card card--c">
    <div class="contact">
      <div class="email">dalemorrow<span class="at">@</span>quillpost.example</div>
      <div class="phone">305.617.4289</div>
      <div class="city">Key West, FL</div>
    </div>
    <div class="chef-name">Chef Dale Morrow</div>
    <div class="tagline">Natural Organic &amp; Health Supportive Cooking</div>
    <div class="web-band">TheHearthRemedy.example</div>
  </section>

  <section class="card card--d">
    <div class="contact">
      <div class="email">dalemorrow<span class="at">@</span>quillpost.example</div>
      <div class="phone">305.617.4289</div>
      <div class="city">Key West, FL</div>
    </div>
    <div class="chef-name">Chef Dale Morrow</div>
    <div class="tagline">Natural Organic &amp; Health Supportive Cooking</div>
    <div class="web-band">TheHearthRemedy.example</div>
  </section>

  <svg class="palette" width="346" height="48" viewBox="0 0 346 48" aria-label="Colour palette">
    <circle cx="23" cy="23" r="23" fill="var(--orange)"/>
    <circle cx="98" cy="23" r="23" fill="var(--blue)"/>
    <circle cx="173" cy="23" r="23" fill="var(--teal)"/>
    <circle cx="247" cy="23" r="23" fill="var(--green)"/>
    <circle cx="322" cy="23" r="23" fill="var(--grey)"/>
  </svg>

</main>
</body>
</html>
```